Mobile Laboratory Design Project Needed

We need a professional brochure made. We are a mobile laboratory service company providing venipuncture, laboratory testing and laboratory consultation services to nursing homes. We would like the brochure made 8 x 11 with the last page being a contact us page and a place to put two business cards.

Target Market(s)

Nursing Home Administrators and Directors of Nursing

Industry/Entity Type

Medical

Colors
0054AA
0677BA
7BADD7
CADEEF
E8F1F8

```html
<!DOCTYPE html>
<html lang="en">
<head>
<meta charset="utf-8">
<title>Harbor Mobile Labs – Tri-fold Brochure</title>
<link href="https://fonts.googleapis.com/css2?family=Merriweather:wght@700;900&family=Montserrat:wght@300;400;600;800&display=swap" rel="stylesheet">
<style>
  :root{
    --blue-deep:#0054AA;
    --blue:#0677BA;
    --blue-royal:#1d5fd0;
    --blue-soft:#7BADD7;
    --blue-pale:#CADEEF;
    --blue-mist:#E8F1F8;
    --paper:#f4f5f6;
    --paper-shade:#dedfe1;
    --ink:#2b3038;
    --night:#2a2428;
    --stage:#1d1d1f;
    --white:#ffffff;
  }
  *{box-sizing:border-box;margin:0;padding:0}
  html,body{width:706px;height:1200px;overflow:hidden;background:var(--stage)}
  body{position:relative;font-family:"Montserrat",sans-serif;color:var(--ink)}

  .spread{position:absolute;left:20px;width:666px;height:515px;overflow:hidden;box-shadow:0 14px 34px rgba(0,0,0,.55)}
  .spread--outside{top:40px;background:linear-gradient(180deg,var(--white),var(--paper-shade))}
  .spread--inside{top:645px;background:var(--paper)}
  .panel{position:absolute;top:0;width:222px;height:515px}
  .panel--left{left:0}.panel--middle{left:222px}.panel--right{left:444px}

  .wave{position:absolute;inset:0;width:666px;height:515px}

  .heading{font-family:"Merriweather",serif;font-weight:900;line-height:1.2;position:absolute;padding-left:9px;border-left:2px solid currentColor}
  .heading--dark{color:var(--ink)}
  .heading--light{color:var(--white)}
  .copy{position:absolute;font-size:8px;line-height:1.5;letter-spacing:.15px}
  .copy--dark{color:var(--ink)}
  .copy--light{color:var(--white)}
  .copy strong{font-weight:600}

  .photo{position:absolute;overflow:hidden}
  .photo--round{border-radius:50%;border:3px solid var(--blue-soft)}

  /* outside left */
  .services-title{left:22px;top:40px;font-size:14px}
  .services-copy{left:22px;top:88px;width:182px}
  .lab-photo{left:132px;top:250px;width:78px;height:78px;background:radial-gradient(circle at 40% 40%,#b89a7a,#5a4636 70%,#2e241d)}
  .who-title{left:22px;top:340px;font-size:13px}
  .who-copy{left:22px;top:362px;width:186px}

  /* outside middle */
  .card-slot{position:absolute;left:21px;width:180px;height:98px;border:1px solid #b9bcc1;border-radius:10px;background:linear-gradient(180deg,#fbfbfb,#ececed);display:flex;align-items:center;justify-content:center;font-family:"Merriweather",serif;font-weight:700;font-size:9px;color:var(--ink)}
  .card-slot--top{top:34px}.card-slot--bottom{top:150px}
  .contact-title{left:22px;top:338px;font-size:13px}
  .contact-list{position:absolute;left:22px;top:366px;width:190px;list-style:none}
  .contact-list li{display:flex;gap:7px;align-items:flex-start;font-size:8px;line-height:1.45;color:var(--white);margin-bottom:6px}
  .contact-list svg{flex:0 0 10px;width:10px;height:10px;margin-top:1px}
  .contact-list .web{font-weight:600}

  /* outside right */
  .cover-top{position:absolute;left:0;top:0;width:222px;height:320px;
    background:radial-gradient(circle at 70% 75%,#e9a35b 0,#7a4a3a 14%,var(--night) 45%,#1f1c24 100%);
    clip-path:path("M0,0 H222 V240 C196,236 156,230 116,238 C70,247 30,290 0,300 Z")}
  .brand{position:absolute;left:0;top:26px;width:222px;display:flex;flex-direction:column;align-items:center;gap:6px}
  .brand-dot{width:38px;height:38px;border-radius:50%;border:2px solid var(--blue-soft)}
  .brand-name{font-family:"Montserrat",sans-serif;font-weight:600;font-size:9px;letter-spacing:1.2px;color:var(--blue-pale);text-transform:uppercase}
  .cover-photo{left:50px;top:118px;width:132px;height:132px;background:radial-gradient(circle at 55% 40%,#f2ede8,#c9b4a6 45%,#8c3a3a 85%)}
  .headline{position:absolute;left:26px;top:296px;color:var(--white);font-size:21px;line-height:1.08;text-transform:uppercase;letter-spacing:.3px}
  .headline .light{font-weight:300;display:block}
  .headline .bold{font-weight:800;display:block}
  .url-bar{position:absolute;left:26px;top:430px;width:172px;height:22px;background:#2d2d30;color:var(--white);font-size:8px;display:flex;align-items:center;justify-content:center;letter-spacing:.2px}

  /* inside left */
  .mission-bg{position:absolute;inset:0;background:linear-gradient(180deg,#f7f9fb 0,#e9eef2 45%,#dde4ea 100%)}
  .mission-photo{left:0;top:258px;width:222px;height:257px;background:linear-gradient(160deg,#eef1f4 0,#c9d3dc 40%,#4a5672 75%,#2d3550 100%)}
  .mission-title{left:22px;top:30px;font-size:13px}
  .mission-copy{left:22px;top:54px;width:186px}

  /* inside middle */
  .services-bg{position:absolute;inset:0;background:linear-gradient(180deg,var(--blue-royal),var(--blue-deep))}
  .service{position:absolute;left:18px;width:190px}
  .service-head{display:flex;align-items:center;gap:9px;padding-bottom:4px;border-bottom:1px solid var(--blue-soft)}
  .service-icon{width:32px;height:32px;flex:0 0 32px}
  .service-name{font-family:"Merriweather",serif;font-weight:900;font-size:11.5px;color:var(--white);line-height:1.15}
  .service p{margin-top:5px;font-size:8px;line-height:1.5;color:var(--white)}
  .service--one{top:26px}.service--two{top:140px}.service--three{top:254px}
  .draw-photo{left:18px;top:380px;width:190px;height:110px;background:linear-gradient(120deg,#dfe6ee 0,#9fb7d6 40%,#2f6fd8 65%,#8a5a4a 100%)}

  /* inside right */
  .menu-bg{position:absolute;inset:0;background:linear-gradient(180deg,#fafafa,#eceded)}
  .menu-title{left:22px;top:30px;font-size:13px}
  .menu-sub{position:absolute;left:22px;top:54px;font-family:"Merriweather",serif;font-weight:900;font-size:10px;color:var(--ink)}
  .menu-copy{left:22px;top:74px;width:184px}
  .test-list{position:absolute;left:22px;top:298px;list-style:none}
  .test-list li{display:flex;align-items:center;gap:6px;font-size:9px;font-weight:600;color:var(--ink);margin-bottom:5px}
  .test-list svg{width:9px;height:9px}
</style>
</head>
<body>

<section class="spread spread--outside" aria-label="Brochure outside">
  <svg class="wave" viewBox="0 0 666 515" aria-hidden="true">
    <defs>
      <linearGradient id="outsideBlue" x1="0" y1="0" x2="1" y2="1">
        <stop offset="0" stop-color="#2a6ee0"/>
        <stop offset="1" stop-color="#0054AA"/>
      </linearGradient>
    </defs>
    <path d="M0,318 C120,270 250,320 360,312 C460,306 500,250 560,238 C600,230 640,236 666,240 L666,515 L0,515 Z" fill="#7BADD7"/>
    <path d="M0,326 C120,282 250,330 360,322 C460,316 500,262 560,250 C600,242 640,248 666,252 L666,515 L0,515 Z" fill="url(#outsideBlue)"/>
  </svg>

  <div class="panel panel--left">
    <h2 class="heading heading--dark services-title">Laboratory and<br>Phlebotomy Services</h2>
    <p class="copy copy--dark services-copy">Harbor Mobile Labs is positively impacting the lives in our community through fast and accurate venipuncture and laboratory testing. Our State licensed and Clinical Quality Council certified laboratory performs testing in the areas of Hematology, Chemistry, Urinalysis, Immunohematology, Coagulation and Microbiology.</p>
    <div class="photo photo--round lab-photo" role="img" aria-label="Photo of a clinical laboratory interior with benches and equipment"></div>
    <h2 class="heading heading--light who-title">Who We Are</h2>
    <p class="copy copy--light who-copy"><strong>Highly qualified and motivated laboratory professionals.</strong> The owners of HML collectively have over 50 years of experience operating and running clinical laboratories across the United States. The company consists of Medical Doctors, Laboratory Directors, Medical Technologists and Phlebotomists that are considered experts in their fields.</p>
  </div>

  <div class="panel panel--middle">
    <div class="card-slot card-slot--top">Place for Business Card</div>
    <div class="card-slot card-slot--bottom">Place for Business Card</div>
    <h2 class="heading heading--light contact-title">Contact us</h2>
    <ul class="contact-list">
      <li><svg viewBox="0 0 10 10" fill="none" stroke="#fff" stroke-width="1"><path d="M5 9.3C3 7 2 5.6 2 4.2a3 3 0 0 1 6 0C8 5.6 7 7 5 9.3Z"/><circle cx="5" cy="4.2" r="1"/></svg><span>418 Cedar Ridge Road, Suite 210, Fairview, Oregon 97024.</span></li>
      <li><svg viewBox="0 0 10 10" fill="none" stroke="#fff" stroke-width="1"><rect x="1" y="2.2" width="8" height="5.8"/><path d="M1 2.4 5 5.6 9 2.4"/></svg><span>admin@harbormobilelabs.com</span></li>
      <li><svg viewBox="0 0 10 10" fill="none" stroke="#fff" stroke-width="1"><path d="M2.2 1.2h1.8l.8 2-1.1.8a5 5 0 0 0 2.3 2.3l.8-1.1 2 .8v1.8c0 .5-.4.9-.9.9A7.7 7.7 0 0 1 1.3 2.1c0-.5.4-.9.9-.9Z"/></svg><span>(555) 014-2280</span></li>
      <li><svg viewBox="0 0 10 10" fill="none" stroke="#fff" stroke-width="1"><circle cx="5" cy="5" r="4"/><ellipse cx="5" cy="5" rx="1.7" ry="4"/><path d="M1 5h8"/></svg><span class="web">www.harbormobilelabs.com</span></li>
    </ul>
  </div>

  <div class="panel panel--right">
    <div class="cover-top"></div>
    <div class="brand">
      <span class="brand-dot"></span>
      <span class="brand-name">Harbor Mobile Labs</span>
    </div>
    <div class="photo photo--round cover-photo" role="img" aria-label="Photo of a doctor speaking with a patient beside blood sample tubes"></div>
    <h1 class="headline">
      <span class="light">Laboratory</span>
      <span class="bold">Results</span>
      <span class="light">That you can</span>
      <span class="bold">Trust</span>
    </h1>
    <div class="url-bar">www.harbormobilelabs.com</div>
  </div>
</section>

<section class="spread spread--inside" aria-label="Brochure inside">
  <div class="panel panel--left">
    <div class="mission-bg"></div>
    <div class="photo mission-photo" role="img" aria-label="Photo of two smiling women reviewing results on a tablet at a desk"></div>
    <h2 class="heading heading--dark mission-title">Our Mission</h2>
    <p class="copy copy--dark mission-copy">There's a notion that to be successful you have to be a huge conglomerate. But we know there is a better way to grow and truly serve the community. That is by making sure what is good for the bottom line is also good for the customer! That is why we created an ecosystem that unites mobile phlebotomy, the clinical laboratory, analytics and machine learning to deliver optimum clinical laboratory services to the communities we serve.</p>
  </div>

  <div class="panel panel--middle">
    <div class="services-bg"></div>
    <div class="service service--one">
      <div class="service-head">
        <svg class="service-icon" viewBox="0 0 32 32" fill="none" stroke="#fff" stroke-width="1.2"><circle cx="16" cy="16" r="15"/><path d="M9 23l9-9M14 11l7 7M19 9l4 4M21 11l-2 2"/><path d="M9 23l-2 2"/></svg>
        <h3 class="service-name">Venipuncture</h3>
      </div>
      <p>Our skilled phlebotomists perform venipuncture with precision and care, ensuring minimal discomfort for our clients.</p>
    </div>
    <div class="service service--two">
      <div class="service-head">
        <svg class="service-icon" viewBox="0 0 32 32" fill="none" stroke="#fff" stroke-width="1.2"><circle cx="16" cy="16" r="15"/><path d="M12 8v7l-4 8h16l-4-8V8M11 8h10"/><path d="M10 20h12"/></svg>
        <h3 class="service-name">Laboratory<br>Testing</h3>
      </div>
      <p>With our advanced laboratory equipment, we conduct a wide range of tests accurately and efficiently.</p>
    </div>
    <div class="service service--three">
      <div class="service-head">
        <svg class="service-icon" viewBox="0 0 32 32" fill="none" stroke="#fff" stroke-width="1.2"><circle cx="16" cy="16" r="15"/><circle cx="11" cy="14" r="2.2"/><circle cx="21" cy="14" r="2.2"/><path d="M7 23c0-3 2-4.5 4-4.5s4 1.5 4 4.5M17 23c0-3 2-4.5 4-4.5s4 1.5 4 4.5"/><path d="M13 8h6v3h-6z"/></svg>
        <h3 class="service-name">Laboratory<br>Consultation</h3>
      </div>
      <p>Our healthcare experts provide professional medical consultation and guidance for individuals and healthcare organizations.</p>
    </div>
    <div class="photo draw-photo" role="img" aria-label="Photo of gloved hands preparing a patient's arm for a blood draw"></div>
  </div>

  <div class="panel panel--right">
    <div class="menu-bg"></div>
    <h2 class="heading heading--dark menu-title">Test Menu</h2>
    <p class="menu-sub">Harbor Mobile Labs</p>
    <p class="copy copy--dark menu-copy">Harbor Mobile Labs has a wide range of laboratory testing that covers the following disease states: Anemia, Bone/Skeleton, Cardiac, Diabetes, Drugs of Abuse, General Chemistry, Hepatic, Immunosuppressant Drugs, Infectious Disease, Inflammatory, Lipids, Microbiology, Mycology, Nutritional Assessment, Oncology, Pancreatic, Parasitology, Prenatal, Renal, Reproductive Endocrinology, Respiratory, Sepsis, Spinal, Therapeutic Drug Monitoring, Metabolic, Toxicology, Urinalysis and Virology.</p>
    <ul class="test-list">
      <li><svg viewBox="0 0 10 10" fill="none" stroke="#0054AA" stroke-width="1"><circle cx="5" cy="5" r="4.3"/><path d="M3 5.2l1.4 1.3L7 3.8"/></svg>Clinical Chemistry</li>
      <li><svg viewBox="0 0 10 10" fill="none" stroke="#0054AA" stroke-width="1"><circle cx="5" cy="5" r="4.3"/><path d="M3 5.2l1.4 1.3L7 3.8"/></svg>Parisitology</li>
      <li><svg viewBox="0 0 10 10" fill="none" stroke="#0054AA" stroke-width="1"><circle cx="5" cy="5" r="4.3"/><path d="M3 5.2l1.4 1.3L7 3.8"/></svg>Immunohematology</li>
      <li><svg viewBox="0 0 10 10" fill="none" stroke="#0054AA" stroke-width="1"><circle cx="5" cy="5" r="4.3"/><path d="M3 5.2l1.4 1.3L7 3.8"/></svg>Mycology</li>
      <li><svg viewBox="0 0 10 10" fill="none" stroke="#0054AA" stroke-width="1"><circle cx="5" cy="5" r="4.3"/><path d="M3 5.2l1.4 1.3L7 3.8"/></svg>Urinalysis</li>
      <li><svg viewBox="0 0 10 10" fill="none" stroke="#0054AA" stroke-width="1"><circle cx="5" cy="5" r="4.3"/><path d="M3 5.2l1.4 1.3L7 3.8"/></svg>Microbiology</li>
      <li><svg viewBox="0 0 10 10" fill="none" stroke="#0054AA" stroke-width="1"><circle cx="5" cy="5" r="4.3"/><path d="M3 5.2l1.4 1.3L7 3.8"/></svg>Virology</li>
      <li><svg viewBox="0 0 10 10" fill="none" stroke="#0054AA" stroke-width="1"><circle cx="5" cy="5" r="4.3"/><path d="M3 5.2l1.4 1.3L7 3.8"/></svg>Tumor Markers</li>
      <li><svg viewBox="0 0 10 10" fill="none" stroke="#0054AA" stroke-width="1"><circle cx="5" cy="5" r="4.3"/><path d="M3 5.2l1.4 1.3L7 3.8"/></svg>Hematology</li>
    </ul>
  </div>
</section>

</body>
</html>
```